Health Coaching Flyer for New Clients

I need a two-sided flyer (3.5" x 8.5" preferred or 5" x 7") to distribute to potential coaching clients. My business name is Talvora Health & Wellness Coaching. My business is focused on helping people with habit changes that contribute to their overall well-being. I would like the design colors to be gender neutral. I would like a small photo of myself near the "my name is Jen" statement. Please feel free to change the logo color to match the design.

Target Market(s)

Adults of all ages.

Font styles to use
Serif

Requirements
Must have
• Emphasize my opening question (found in health coaching brochure - attached).
• Small picture of myself near "my name is Jen" statement.
Should not have
• No light of pastel colors.

```html
<!DOCTYPE html>
<html lang="en">
<head>
<meta charset="utf-8">
<title>Talvora Health &amp; Wellness Coaching – Flyer</title>
<link href="https://fonts.googleapis.com/css2?family=Montserrat:wght@400;500;700;800&family=Oswald:wght@600&display=swap" rel="stylesheet">
<style>
  :root{
    --canvas:#d6d6d6;
    --paper:#ffffff;
    --ink:#2b2b2b;
    --ink-soft:#3c3c3c;
    --black:#050505;
    --sq1:#b4b4b4;--sq2:#8d8d8d;--sq3:#5e5e5e;--sq4:#373737;--sq5:#101010;
  }
  *{margin:0;padding:0;box-sizing:border-box}
  html,body{width:1200px;height:1200px;overflow:hidden;background:var(--canvas)}
  body{position:relative;font-family:"Montserrat",sans-serif;color:var(--ink)}
  .flyer{position:absolute;top:116px;width:399px;height:968px;background:linear-gradient(180deg,#fff 0%,#f3f3f3 55%,#fff 100%);overflow:hidden}
  .flyer--front{left:161px}
  .flyer--back{left:684px}

  .brand{position:absolute;top:0;left:0;width:399px;height:94px;background:var(--paper);text-align:center;padding-top:30px}
  .brand__name{font-family:"Montserrat",sans-serif;font-weight:800;font-size:31px;letter-spacing:3px;line-height:1;color:var(--black)}
  .brand__tag{font-family:"Montserrat",sans-serif;font-weight:800;font-size:8px;letter-spacing:.2px;color:var(--black);margin-top:4px}

  .stripe{position:absolute;left:0;width:399px;height:12px}
  .stripe span{position:absolute;top:0;width:12px;height:11px}
  .stripe .bar{height:11px}

  .photo{position:absolute;left:0;width:399px}
  .photo--landscape{top:111px;height:389px;background:linear-gradient(180deg,#b9d3de 0%,#8c9b72 30%,#5f7040 55%,#6f9a46 68%,#4f7c99 78%,#5b87a3 86%,#6e5733 94%,#4d3b22 100%)}
  .photo--family{top:0;height:265px;background:linear-gradient(160deg,#f3e2b0 0%,#c8b17a 25%,#9aa66a 50%,#7d9ec8 70%,#4f6d3a 100%)}

  .headline{position:absolute;left:20px;width:359px;font-family:"Oswald",sans-serif;font-weight:600;font-size:23.5px;line-height:31px;color:var(--ink);text-align:center;letter-spacing:-.2px}
  .front-headline{top:560px}
  .back-headline{top:305px;left:32px;text-align:left;width:350px}

  .intro{position:absolute;top:660px;left:41px;width:309px;font-size:11.6px;line-height:15.2px;letter-spacing:.6px;text-align:justify;text-align-last:center;color:var(--ink-soft);hyphens:auto}

  .portrait{position:absolute;right:0;top:779px;width:138px;height:189px;border-radius:60px 60px 0 0;background:linear-gradient(180deg,#3a2f2a 0%,#9c6b4e 45%,#1a1614 100%)}

  .contact{position:absolute;left:0;top:872px;width:399px;height:96px;background:var(--black);color:#fff;padding:10px 0 0 26px}
  .contact__lead{font-size:10.6px;line-height:13.5px;letter-spacing:.3px}
  .contact__name{font-weight:800;font-size:10.6px;margin-top:8px;letter-spacing:.2px}
  .contact__info{font-size:10.6px;margin-top:5px;letter-spacing:.2px}

  .benefits{position:absolute;top:358px;left:0;width:399px;height:286px}
  .benefits__line{position:absolute;left:51px;top:4px;width:1.5px;height:278px;background:var(--ink)}
  .benefits__dot{position:absolute;left:48.5px;width:6px;height:6px;border-radius:50%;background:var(--ink)}
  .benefit{position:absolute;left:0;width:399px}
  .benefit__icon{position:absolute;left:33px;width:38px;height:38px;border:1.5px solid var(--ink);border-radius:50%;background:#fff}
  .benefit__icon svg{width:100%;height:100%}
  .benefit__text{position:absolute;left:84px;width:260px;font-size:11.6px;line-height:15.2px;letter-spacing:.6px;color:var(--ink-soft);white-space:nowrap}

  .invite{position:absolute;left:40px;width:327px;font-size:11.6px;line-height:15.2px;letter-spacing:.6px;text-align:justify;color:var(--ink-soft);hyphens:auto}
</style>
</head>
<body>

<section class="flyer flyer--front">
  <header class="brand">
    <div class="brand__name">TALVORA</div>
    <div class="brand__tag">HEALTH &amp; WELLNESS COACHING</div>
  </header>

  <div class="stripe" style="top:94px">
    <span style="left:27px;background:var(--sq1)"></span>
    <span style="left:47px;background:var(--sq2)"></span>
    <span style="left:67px;background:var(--sq3)"></span>
    <span style="left:87px;background:var(--sq4)"></span>
    <span style="left:107px;background:var(--sq5)"></span>
    <span class="bar" style="left:126px;width:273px;background:var(--black)"></span>
  </div>

  <div class="photo photo--landscape" role="img" aria-label="Woman in a yoga tree pose on a rocky shore before green mountain peaks and a calm blue lake"></div>

  <div class="stripe" style="top:508px">
    <span class="bar" style="left:0;width:276px;background:var(--black)"></span>
    <span style="left:283px;background:var(--sq5)"></span>
    <span style="left:303px;background:var(--sq4)"></span>
    <span style="left:323px;background:var(--sq3)"></span>
    <span style="left:343px;background:var(--sq2)"></span>
    <span style="left:363px;background:var(--sq2);opacity:.8"></span>
  </div>

  <h1 class="headline front-headline">NEED SUPPORT IN MAKING<br>REAL, LASTING LIFESTYLE AND<br>BEHAVIOR CHANGES?</h1>

  <p class="intro">My name is Jen.&nbsp; I am studying to become an THRIVE-Certified Functional Health Coach.&nbsp; My training involves many science-based practices that improve both our health and how we grow and change as humans.&nbsp; I now have the opportunity to turn that knowledge into practice by coaching actual clients interested in improving their own health and well-being.</p>

  <div class="stripe" style="top:859px">
    <span style="left:0;background:var(--sq1)"></span>
    <span style="left:20px;background:var(--sq2)"></span>
    <span style="left:40px;background:var(--sq3)"></span>
    <span style="left:61px;background:var(--sq4)"></span>
    <span style="left:81px;background:var(--sq5)"></span>
    <span class="bar" style="left:100px;width:180px;background:var(--black)"></span>
  </div>

  <footer class="contact">
    <p class="contact__lead">Please contact me.&nbsp; I’m ready to support<br>you as you work to improve your health.</p>
    <p class="contact__name">JEN TALVORA</p>
    <p class="contact__info">555-014-2276 | talvorahwc@example.com</p>
  </footer>

  <div class="portrait" role="img" aria-label="Portrait photo of Jen, the coach"></div>
</section>

<section class="flyer flyer--back">
  <div class="photo photo--family" role="img" aria-label="Smiling family of four sitting together on a blanket in a sunlit meadow"></div>

  <div class="stripe" style="top:270px">
    <span class="bar" style="left:0;width:276px;background:var(--black)"></span>
    <span style="left:283px;background:var(--sq5)"></span>
    <span style="left:303px;background:var(--sq4)"></span>
    <span style="left:323px;background:var(--sq3)"></span>
    <span style="left:343px;background:var(--sq2)"></span>
    <span style="left:363px;background:var(--sq2);opacity:.8"></span>
  </div>

  <h2 class="headline back-headline">FUNCTIONAL HEALTH COACHES…</h2>

  <div class="benefits">
    <div class="benefits__line"></div>
    <div class="benefits__dot" style="top:1px"></div>
    <div class="benefits__dot" style="top:280px"></div>

    <div class="benefit" style="top:20px">
      <div class="benefit__icon"><svg viewBox="0 0 38 38" fill="none" stroke="#2b2b2b" stroke-width="1.2"><rect x="12" y="9" width="14" height="18"/><line x1="15" y1="14" x2="23" y2="14"/><line x1="15" y1="18" x2="23" y2="18"/><line x1="15" y1="22" x2="20" y2="22"/></svg></div>
      <p class="benefit__text" style="top:7px">Leverage your strengths rather than<br>focus on your weaknesses</p>
    </div>
    <div class="benefit" style="top:66px">
      <div class="benefit__icon"><svg viewBox="0 0 38 38" fill="none" stroke="#2b2b2b" stroke-width="1.2"><path d="M10 12h18v11H17l-5 4v-4h-2z"/></svg></div>
      <p class="benefit__text" style="top:7px">Support you in finding your own<br>strategies and motivation for change</p>
    </div>
    <div class="benefit" style="top:112px">
      <div class="benefit__icon"><svg viewBox="0 0 38 38" fill="none" stroke="#2b2b2b" stroke-width="1.2"><line x1="19" y1="9" x2="19" y2="28"/><line x1="11" y1="13" x2="27" y2="13"/><path d="M11 13l-3 7h6z"/><path d="M27 13l-3 7h6z"/><line x1="14" y1="28" x2="24" y2="28"/></svg></div>
      <p class="benefit__text" style="top:7px">Provide a judgment-free zone and<br>support your autonomy</p>
    </div>
    <div class="benefit" style="top:158px">
      <div class="benefit__icon"><svg viewBox="0 0 38 38" fill="none" stroke="#2b2b2b" stroke-width="1.2"><path d="M10 17l15-7 2 4-15 7z"/><line x1="18" y1="18" x2="13" y2="28"/><line x1="18" y1="18" x2="23" y2="28"/></svg></div>
      <p class="benefit__text" style="top:7px">Use an experimental mindset to find<br>and develop sustainable habits</p>
    </div>
    <div class="benefit" style="top:222px">
      <div class="benefit__icon"><svg viewBox="0 0 38 38" fill="none" stroke="#2b2b2b" stroke-width="1.2"><circle cx="19" cy="19" r="4"/><circle cx="19" cy="10" r="1.5"/><circle cx="19" cy="28" r="1.5"/><circle cx="10" cy="19" r="1.5"/><circle cx="28" cy="19" r="1.5"/><circle cx="12.5" cy="12.5" r="1.5"/><circle cx="25.5" cy="25.5" r="1.5"/><circle cx="25.5" cy="12.5" r="1.5"/><circle cx="12.5" cy="25.5" r="1.5"/></svg></div>
      <p class="benefit__text" style="top:-10px">Act as your accountability partner as<br>you reach your unique health goals;<br>whether they be improving sleep,<br>diet, fitness, social connection,<br>or reducing stress.</p>
    </div>
  </div>

  <p class="invite" style="top:665px">I would like to invite you to participate with me as a client as I continue to hone my coaching skills.&nbsp; We can develop a plan and schedule that aligns with your goals.</p>
  <p class="invite" style="top:741px">As a way to give back to my community, I am offering new clients six free coaching sessions.&nbsp; This is a limited time offer.</p>

  <div class="stripe" style="top:859px">
    <span style="left:0;background:var(--sq1)"></span>
    <span style="left:20px;background:var(--sq2)"></span>
    <span style="left:40px;background:var(--sq3)"></span>
    <span style="left:61px;background:var(--sq4)"></span>
    <span style="left:81px;background:var(--sq5)"></span>
    <span class="bar" style="left:100px;width:180px;background:var(--black)"></span>
  </div>

  <footer class="contact">
    <p class="contact__lead">Please contact me.&nbsp; I’m ready to support<br>you as you work to improve your health.</p>
    <p class="contact__name">JEN TALVORA</p>
    <p class="contact__info">555-014-2276 | talvorahwc@example.com</p>
  </footer>

  <div class="portrait" role="img" aria-label="Portrait photo of Jen, the coach"></div>
</section>

</body>
</html>
```